Halvorne Partners Banner Add

We are an international headhunting firm looking to target IT guys in Europe and USA to come and work in Singapore or Sydney (Australia). These guys will generally work in Trading firms / Banks / Top Tech Firms. Text - "Are you working in the Fin/ Tech space for a bank or High Frequency Trading firm as a technologist?We have your job in Singapore/ Sydney.Better / Great LifestyleWorking visa'sThe highest calibre clients.Bored with Brexit?Apply now.We need 5 pictures to rotate on a banner add to attract attention / represent this call to action.Some ideas… Guy on a laptop on a beach Sydney Skyline Singapore Skyline Bondi Beach Paradise beach picturesPeople playing on Beach London in the rain vs Sydney (sunny)Style needs to be classy, premium, well finished, boutique and in keeping with our website www.halvorne-partners.com. - hence any text you think could be worthwhile taking from there is fine.File formats: JPG, PNG, GIF Maximum file size: 3MB Media Sizes: Minimum: 600 × 315 pixels Recommended: 1200 × 628 pixels Image ratio: 1.91:1 To maximize advert delivery, Images need to be public property, no copyright. 5 rotating pictures incorporating the text, pictures and sell to create one banner add.

Target Market(s)

Banking/ Finance

Number of Pages Required

1 page

Requirements
Must have
• 5 different banners on rotate
Nice to have
• Classy, text suggested or snippets of as required, maybe black and white to match our logo's but injections of colour but full colour is also fine I could be converted.
Should not have
• not too flashy, should be elegant, classy pictures, clean like our website.
• www.halvorne-partners.com

```html
<!DOCTYPE html>
<html lang="en">
<head>
<meta charset="utf-8">
<title>Halvorne Partners – Technologist Roles in Singapore</title>
<link rel="stylesheet" href="https://fonts.googleapis.com/css2?family=Jost:wght@300;400;700&display=swap">
<style>
  :root {
    --sky-top: #1c181c;
    --sky-mid: #3a2c31;
    --sky-glow: #6a4a4b;
    --horizon: #4a3a3a;
    --water-top: #2e2a2d;
    --water-bottom: #1d1c20;
    --panel: rgba(12, 9, 10, 0.86);
    --ink-light: #ffffff;
    --ink-soft: #e6e3e3;
    --button-bg: #ffffff;
    --button-ink: #2a2628;
  }

  html, body {
    margin: 0;
    padding: 0;
    width: 1200px;
    height: 628px;
    overflow: hidden;
    background: #000;
  }

  .banner {
    position: relative;
    width: 1200px;
    height: 628px;
    overflow: hidden;
    font-family: "Jost", "Futura", sans-serif;
  }

  .banner__scene {
    position: absolute;
    inset: 0;
    background:
      radial-gradient(ellipse 520px 180px at 820px 250px, rgba(150, 100, 95, 0.45), transparent 70%),
      radial-gradient(ellipse 420px 150px at 220px 380px, rgba(140, 90, 80, 0.35), transparent 70%),
      linear-gradient(180deg,
        var(--sky-top) 0%,
        var(--sky-mid) 30%,
        var(--sky-glow) 58%,
        var(--horizon) 74%,
        var(--water-top) 80%,
        var(--water-bottom) 100%);
  }

  .banner__panel {
    position: absolute;
    left: 409px;
    top: 23px;
    width: 383px;
    height: 605px;
    background: var(--panel);
    text-align: center;
    color: var(--ink-light);
  }

  .headline {
    margin: 0;
    position: absolute;
    left: 0;
    right: 0;
    top: 88px;
    font-weight: 700;
    text-transform: uppercase;
    letter-spacing: 0.06em;
    line-height: 1;
  }

  .headline__line {
    display: block;
  }

  .headline__line--small {
    font-size: 34px;
  }

  .headline__line--large {
    font-size: 38px;
    margin-top: 14px;
  }

  .offer {
    margin: 0;
    position: absolute;
    left: 0;
    right: 0;
    top: 220px;
    font-weight: 300;
    font-size: 34px;
    letter-spacing: 0.05em;
    line-height: 48px;
    text-transform: uppercase;
  }

  .offer__place {
    font-weight: 700;
  }

  .apply-button {
    position: absolute;
    left: 39px;
    top: 368px;
    width: 304px;
    height: 75px;
    background: var(--button-bg);
    color: var(--button-ink);
    font-weight: 300;
    font-size: 26px;
    letter-spacing: 0.06em;
    line-height: 75px;
    text-decoration: none;
    text-transform: uppercase;
  }

  .sectors {
    margin: 0;
    position: absolute;
    left: 0;
    right: 0;
    top: 471px;
    font-weight: 300;
    font-size: 18.5px;
    letter-spacing: 0.04em;
    line-height: 27px;
    color: var(--ink-soft);
  }

  .sectors span {
    display: block;
  }
</style>
</head>
<body>
  <main class="banner">
    <div class="banner__scene" role="img"
         aria-label="Night photograph of the Singapore waterfront skyline reflected in the bay, with a lit tri-tower resort on the left and an illuminated observation wheel on the right under a hazy reddish sky"></div>

    <section class="banner__panel">
      <h1 class="headline">
        <span class="headline__line headline__line--small">Are you a</span>
        <span class="headline__line headline__line--large">Technologist?</span>
      </h1>

      <p class="offer">
        We have a<br>
        Job for you<br>
        at <span class="offer__place">Singapore</span>
      </p>

      <a class="apply-button" href="#">Apply Now</a>

      <p class="sectors">
        <span>Finance &amp; Technology Space</span>
        <span>Major Banks &amp;</span>
        <span>High Frequency Trading Firms</span>
      </p>
    </section>
  </main>
</body>
</html>
```